Q R Ventral Harbor Works, LLC
I just posted pic to use....
where we can find the details for this project....can u upload it in pdf format...so we can start designing it..
Sorry looking for a Trifold brochure

```html
<!DOCTYPE html>
<html lang="en">
<head>
<meta charset="utf-8">
<title>Q R Ventral Harbor Works, LLC — Trifold Brochure</title>
<link href="https://fonts.googleapis.com/css2?family=Open+Sans:wght@400;600;700;800&family=Cinzel:wght@700&display=swap" rel="stylesheet">
<style>
  :root{
    --page:#e9e7e4;
    --paper:#ffffff;
    --navy:#13325c;
    --navy-deep:#0b2142;
    --blue:#2f6fb3;
    --sky:#8fc0e8;
    --orange:#ea8a26;
    --ink:#2b2b2b;
    --muted:#6c6c6c;
    --rule:#c9d3df;
  }
  *{box-sizing:border-box;margin:0;padding:0}
  html,body{width:1200px;height:545px;overflow:hidden;background:var(--page)}
  body{font-family:"Open Sans",Arial,sans-serif;color:var(--ink);position:relative}
  .sheet{position:absolute;top:14px;width:584px;height:516px;display:flex;background:var(--paper);box-shadow:0 2px 6px rgba(0,0,0,.25)}
  .sheet--outside{left:8px}
  .sheet--inside{left:606px}
  .panel{width:194.6px;height:100%;position:relative;overflow:hidden;border-right:1px solid #eee}
  .panel:last-child{border-right:none}
  .copy{font-size:5.6px;line-height:1.55;color:var(--muted);text-align:justify}
  .copy p{margin-bottom:4px}
  .band{background:linear-gradient(180deg,var(--navy),var(--navy-deep));color:#fff;display:flex;align-items:center;gap:5px;padding:0 8px;height:20px;font-size:7.5px;font-weight:700;letter-spacing:.5px;text-transform:uppercase}
  .dot{width:14px;height:14px;border-radius:50%;background:var(--orange);border:2px solid #fff;flex:none}
  .brand{display:flex;align-items:center;gap:5px}
  .brand__mark{width:18px;height:18px;background:var(--orange);flex:none}
  .brand__name{font-size:8px;font-weight:700;color:var(--navy);line-height:1.1}
  .photo{background:linear-gradient(160deg,var(--sky),var(--blue) 60%,var(--navy))}
  .web{position:absolute;left:0;right:0;bottom:0;height:20px;background:var(--navy);color:#fff;font-size:6.5px;display:flex;align-items:center;justify-content:center;letter-spacing:.3px}
  .list{list-style:none;font-size:5.8px;color:var(--muted);line-height:1.7}
  .list li::before{content:"";display:inline-block;width:4px;height:4px;background:var(--orange);margin-right:4px;vertical-align:middle}
  h3.sub{font-size:6.8px;color:var(--orange);font-weight:700;margin:4px 0 2px}

  /* outside: back panel */
  .about-text{padding:14px 12px}
  .about-text h2{font-size:10px;font-weight:800;color:var(--navy);margin-bottom:6px;line-height:1.2}

  /* outside: middle panel */
  .mid-top{margin-top:12px}
  .mid-brand{padding:12px 10px 6px}
  .mid-body{padding:0 10px}
  .contact{position:absolute;left:0;right:0;top:330px}
  .contact .copy{padding:8px 10px}
  .contact address{font-style:normal;font-size:5.8px;line-height:1.7;color:var(--muted);padding:0 10px}

  /* outside: cover */
  .cover .brand{padding:80px 0 0 62px}
  .cover__title{margin:26px 0 0 18px;font-family:"Cinzel",serif;color:var(--navy-deep);font-size:14px;line-height:1.35;text-align:center;width:160px}
  .cover__title small{display:block;font-size:9px}
  .cover__photo{position:absolute;left:0;right:0;top:235px;bottom:20px}

  /* inside */
  .mission .band{margin-top:14px}
  .mission .copy{padding:8px 10px}
  .globe{height:95px;margin:0 10px;background:radial-gradient(circle at 45% 45%,var(--sky),var(--blue) 55%,var(--navy-deep))}
  .services .band{margin-top:14px;justify-content:flex-end}
  .services .copy{padding:8px 10px 2px}
  .svc{display:flex;gap:6px;padding:4px 10px}
  .svc__thumb{width:34px;height:34px;flex:none}
  .svc__body h3.sub{margin-top:0}
  .city{height:60px;margin-top:0;background:linear-gradient(180deg,#cfe3f4,var(--blue) 70%,var(--navy))}
  .hco .band{height:18px;font-size:6.8px}
  .hco .copy{padding:8px 10px 4px}
  .hco .list{padding:0 10px}
</style>
</head>
<body>

<section class="sheet sheet--outside" aria-label="Brochure outside">
  <div class="panel about-text">
    <h2>Q R Ventral Harbor Works, LLC</h2>
    <div class="copy">
      <p>Q R Ventral Harbor Works, LLC is a business consultancy serving public agencies and private firms. We help clients plan clearly, manage resources well and deliver lasting results across every stage of their work.</p>
      <p>Our team brings years of hands-on practice in program oversight, logistics, staffing and technology. We listen first, then shape solutions that fit each client and each budget.</p>
      <p>We believe that strong partnerships are built on trust, steady communication and measurable outcomes. Every engagement is led by a senior advisor who stays with the project from start to finish.</p>
      <p>From a single task to a full program, we offer complete and sustainable support so that our clients can focus on their mission with confidence.</p>
    </div>
  </div>

  <div class="panel">
    <div class="band mid-top"><span class="dot"></span>About Us</div>
    <div class="brand mid-brand"><span class="brand__mark"></span><span class="brand__name">Q R Ventral Harbor Works, LLC</span></div>
    <div class="mid-body">
      <div class="copy"><p>We deliver dependable consulting with a focus on quality, value and accountability for every client we serve.</p></div>
      <ul class="list">
        <li>Strategic planning and management</li>
        <li>Program and project management</li>
        <li>Compliance and logistics support</li>
        <li>Information technology services</li>
        <li>Human capital outsourcing</li>
      </ul>
    </div>
    <div class="contact">
      <div class="band"><span class="dot"></span>Contact</div>
      <div class="copy"><p>To find out how we can help your organization, reach out to our team today.</p></div>
      <address>
        Q R Ventral Harbor Works, LLC<br>
        1420 Ledger Row, Suite 8<br>
        Fairhaven, ST 20450<br>
        (555) 014-2290<br>
        hello@qrventralharborworks.com
      </address>
    </div>
  </div>

  <div class="panel cover">
    <div class="brand"><span class="brand__mark"></span><span class="brand__name">Q R Ventral<br>Harbor Works</span></div>
    <h1 class="cover__title">Complete and Sustainable<small>Solutions from A to Z</small></h1>
    <div class="cover__photo photo" role="img" aria-label="Photo of a business team at work"></div>
    <div class="web">qrventralharborworks.com</div>
  </div>
</section>

<section class="sheet sheet--inside" aria-label="Brochure inside">
  <div class="panel mission">
    <div class="band"><span class="dot"></span>Our Mission and Philosophy</div>
    <div class="copy">
      <p>Our mission is to give every client practical, proven solutions that improve performance and reduce risk. We combine careful planning with hands-on delivery.</p>
      <p>We value honesty, teamwork and results, and we measure our success by the success of the people we serve.</p>
    </div>
    <div class="globe" role="img" aria-label="Illustration of a glowing globe"></div>
    <div class="copy">
      <h3 class="sub">What Distinguishes Q R Ventral</h3>
      <p>Senior advisors lead each engagement, clear reporting keeps clients informed, and flexible teams scale up or down as needs change.</p>
      <p>We stay with our clients long after launch to make sure results last.</p>
    </div>
  </div>

  <div class="panel services">
    <div class="band">Our Services<span class="dot"></span></div>
    <div class="copy"><p>We offer a broad range of services to help organizations plan, run and improve their operations.</p></div>
    <div class="svc"><div class="svc__thumb photo" role="img" aria-label="Photo of a planning meeting"></div><div class="svc__body copy"><h3 class="sub">Planning and Management</h3><p>Goals, roadmaps and budgets built around your priorities.</p></div></div>
    <div class="svc"><div class="svc__thumb photo" role="img" aria-label="Photo of a project review"></div><div class="svc__body copy"><h3 class="sub">Program Management</h3><p>Schedules, staffing and oversight for complex programs.</p></div></div>
    <div class="svc"><div class="svc__thumb photo" role="img" aria-label="Photo of a warehouse"></div><div class="svc__body copy"><h3 class="sub">Compliance and Logistics</h3><p>Rules, records and supply chains kept in good order.</p></div></div>
    <div class="svc"><div class="svc__thumb photo" role="img" aria-label="Photo of computer screens"></div><div class="svc__body copy"><h3 class="sub">Information Technology</h3><p>Systems, networks and support that keep work moving.</p></div></div>
  </div>

  <div class="panel hco">
    <div class="city" role="img" aria-label="Photo of a city skyline"></div>
    <div class="band"><span class="dot"></span>Human Capital Outsourcing</div>
    <div class="copy"><p>We provide skilled people for short and long term needs, matched carefully to the role and ready to contribute from day one.</p></div>
    <ul class="list">
      <li>Business analysts</li>
      <li>Program managers</li>
      <li>Administrative staff</li>
      <li>Logistics specialists</li>
      <li>IT support technicians</li>
      <li>Finance and budget staff</li>
      <li>Training coordinators</li>
    </ul>
    <div class="web">qrventralharborworks.com</div>
  </div>
</section>

</body>
</html>
```